依頼詳細
シンプル・お洒落・高級感
記載項目
会社名・役職・氏名・住所・☎・FAX・携帯番号・パソコンアド・携帯アド
その他おまかせします。
希望イメージ
シンプル 複雑
単色 カラフル
暗い 明るい
日常 高級
遊び心 厳粛
未来的 伝統的
女性的 男性的
希望する色
希望は特にありません。
納品ファイル
• 高解像度JPG (.jpg)
• イラストレーター形式 (.ai)
補足説明
■ 選んだ理由

シンプルかつお洒落でした。

■ 提案者全員のお礼・コメント

たくさんのご提案有難うございました。

```html
<!DOCTYPE html>
<html lang="ja">
<head>
<meta charset="utf-8">
<title>名刺 — 株式会社ノルヴェル</title>
<link href="https://fonts.googleapis.com/css2?family=Noto+Sans+JP:wght@300;400;500&display=swap" rel="stylesheet">
<style>
  :root{
    --bg:#e9e9e9;
    --card:#ffffff;
    --accent:#2b9ad8;
    --dark:#2a2220;
    --text:#3a3a3a;
    --muted:#6a6a6a;
    --rule:#9a9a9a;
  }
  *{margin:0;padding:0;box-sizing:border-box}
  html,body{width:867px;height:1200px;overflow:hidden;background:var(--bg)}
  body{font-family:"Noto Sans JP",sans-serif;color:var(--text)}
  .card{position:absolute;left:118px;top:100px;width:628px;height:1010px;background:var(--card)}
  .side-bar{position:absolute;left:0;top:0;width:32px;height:100%;background:var(--dark)}
  .side-bar::before{content:"";position:absolute;left:0;top:0;width:100%;height:190px;background:var(--accent)}
  .brand{position:absolute;left:95px;top:200px;font-size:32px;font-weight:400;color:var(--dark);letter-spacing:1px;line-height:1}
  .title{position:absolute;left:95px;top:356px;font-size:17px;font-weight:300;letter-spacing:2px;line-height:1}
  .name-row{position:absolute;left:95px;top:396px;width:440px;height:68px;border-bottom:2px solid var(--rule);display:flex;align-items:flex-end;gap:28px;padding-bottom:8px}
  .name{font-size:42px;font-weight:400;letter-spacing:8px;color:var(--dark);line-height:1}
  .name-roman{font-size:16px;font-weight:300;color:var(--muted);line-height:1.4}
  .contact-list{position:absolute;left:95px;list-style:none}
  .contact-list li{display:flex;align-items:center;gap:10px;height:34px;font-size:18px;font-weight:300;color:var(--muted)}
  .contact-list.personal{top:512px}
  .contact-list.office{top:702px}
  .contact-list .indent{padding-left:28px}
  .icon{width:18px;height:18px;flex:none}
  .company{position:absolute;left:95px;top:658px;font-size:25px;font-weight:500;color:var(--accent);letter-spacing:1px;line-height:1}
</style>
</head>
<body>
<div class="card">
  <div class="side-bar"></div>

  <p class="brand">Norvelle</p>

  <p class="title">代表取締役</p>
  <div class="name-row">
    <span class="name">山田 太郎</span>
    <span class="name-roman">Taro Yamada</span>
  </div>

  <ul class="contact-list personal">
    <li>
      <svg class="icon" viewBox="0 0 18 18"><rect width="18" height="18" rx="2" fill="var(--dark)"/><rect x="6" y="3" width="6" height="12" rx="1" fill="none" stroke="#fff" stroke-width="1.5"/></svg>
      090-0000-0000
    </li>
    <li>
      <svg class="icon" viewBox="0 0 18 18"><rect width="18" height="18" rx="2" fill="var(--dark)"/><rect x="3" y="4" width="12" height="8" fill="none" stroke="#fff" stroke-width="1.5"/><rect x="6" y="13" width="6" height="1.5" fill="#fff"/></svg>
      PC: ○○○○@○○○○○○○○
    </li>
    <li class="indent">Mobile: ○○○○○@○○○○○○○○</li>
  </ul>

  <p class="company">株式会社ノルヴェル</p>

  <ul class="contact-list office">
    <li>
      <svg class="icon" viewBox="0 0 18 18"><rect width="18" height="18" rx="2" fill="var(--dark)"/><path d="M5 5h8M5 8h8M9 8v6" stroke="#fff" stroke-width="1.6" fill="none"/></svg>
      〒100-0001 東京都千代田区緑町 1-1-1
    </li>
    <li class="indent">緑町ビル 1F</li>
    <li>
      <svg class="icon" viewBox="0 0 18 18"><rect width="18" height="18" rx="2" fill="var(--dark)"/><path d="M5 4c-1 1-1 3 1 6s4 4 6 4l1-2-2-1.5-1 1c-1-.5-2.5-2-3-3l1-1L6.5 3.5z" fill="#fff"/></svg>
      Tel. 03-0000-0001
    </li>
    <li>
      <svg class="icon" viewBox="0 0 18 18"><rect width="18" height="18" rx="2" fill="var(--dark)"/><rect x="4" y="7" width="10" height="7" fill="none" stroke="#fff" stroke-width="1.5"/><rect x="6" y="3" width="6" height="4" fill="none" stroke="#fff" stroke-width="1.3"/></svg>
      Fax 03-0000-0002
    </li>
  </ul>
</div>
</body>
</html>
```